Fun/Happy Business Card & New Logo for Home Cake Shop

We need a business card for a small home-based, 2 person husband/wife bakery where we do cakes, cupcakes, eclairs, cream puffs and such. Our company name is Tiny Sunny Bakes.

We generally like the colour pink, but are open to other colour scheme ideas as well. The head chef(wife) is a very fun-loving, always cheerful and happy person and we want the business card to reflect her bubbly personality.

The business card should contain the husband's name AND the wife's name.
Updates

1st place prize money has been increased as requested. Thanks for your designs so far! 

Target Market(s)

Generally adults, for birthdays or small/medium sized catering events.

Industry/Entity Type

Bakery

Requirements
Must have
• Name 1: Marisol Tan
Phone: 93816257

Name 2: Koren Tan
Phone: 97421560

Email: info@tinysunnybakes.example
Website: www.tinysunnybakes.example

Additional Info, Edit: Please ensure that the logo contains a cake and at least a couple cupcakes.
Nice to have
• I have uploaded a couple images with the general feel of what we want. The logo should be one with a cake and some cupcakes around it, with the words Tiny Sunny Bakes. Try to come up with something more impressive than the current logo we have.

For the draft name card I uploaded in the file, that is also what we're sort of looking at. Try to come up with something more impressive/creative than that name card as well.

For the back of the name card, we are happy with just having the logo there. We're not sure what colour scheme would go best just yet, so feel free to show us your creative minds! :)

Additional Info, Edit: Please try to come up with a more realistic type of cake and cupcakes in the logo. We do not want it to be too cartoony. The attached images are just examples of the format.
Should not have
• Wordings or images that indicate 'Phone', 'Email' or 'Website' do not need to be included. Our customer base should be able to identify what an email and a website looks like. However, if you find that it looks particularly better, then feel free to be creative.

```html
<!DOCTYPE html>
<html lang="en">
<head>
<meta charset="utf-8">
<title>Tiny Sunny Bakes – Business Card</title>
<link rel="stylesheet" href="https://fonts.googleapis.com/css2?family=Dancing+Script:wght@400&family=Delius&family=Pathway+Gothic+One&display=swap">
<style>
  :root {
    --page: #ffffff;
    --card: #8e4899;
    --card-ink: #ffffff;
    --label-ink: #111111;
    --logo-pink: #f06aa8;
    --logo-blush: #f7b6cf;
  }
  * { margin: 0; padding: 0; box-sizing: border-box; }
  html, body { width: 1200px; height: 557px; overflow: hidden; background: var(--page); }
  .canvas { position: relative; width: 1200px; height: 557px; }

  .card {
    position: absolute;
    top: 137px;
    width: 445px;
    height: 253px;
    background: var(--card);
    color: var(--card-ink);
  }
  .card--back { left: 70px; }
  .card--front { left: 668px; }

  .contact {
    position: absolute;
    top: 22px;
    text-align: center;
  }
  .contact--husband { left: 16px; width: 170px; }
  .contact--wife { right: 12px; width: 180px; }
  .contact__name {
    font-family: "Dancing Script", cursive;
    font-size: 34px;
    line-height: 1.2;
    letter-spacing: 0.5px;
  }
  .contact__phone {
    font-family: "Delius", sans-serif;
    font-size: 22px;
    margin-top: 8px;
  }

  .web-details {
    position: absolute;
    left: 0;
    right: 0;
    top: 176px;
    text-align: center;
    font-family: "Delius", sans-serif;
    font-size: 16px;
    line-height: 21px;
  }

  .brand-mark {
    position: absolute;
    left: 130px;
    top: 6px;
    width: 186px;
    height: 156px;
  }
  .brand-name {
    position: absolute;
    left: 0;
    right: 0;
    top: 170px;
    text-align: center;
    font-family: "Dancing Script", cursive;
    font-size: 50px;
    line-height: 1;
  }

  .side-label {
    position: absolute;
    top: 410px;
    width: 200px;
    text-align: center;
    font-family: "Pathway Gothic One", sans-serif;
    font-size: 46px;
    color: var(--label-ink);
  }
  .side-label--back { left: 192px; }
  .side-label--front { left: 790px; }
</style>
</head>
<body>
<main class="canvas">
  <section class="card card--back">
    <div class="contact contact--husband">
      <p class="contact__name">Koren Tan</p>
      <p class="contact__phone">97421560</p>
    </div>
    <div class="contact contact--wife">
      <p class="contact__name">Marisol Tan</p>
      <p class="contact__phone">93816257</p>
    </div>
    <div class="web-details">
      <p>Email info@tinysunnybakes.example</p>
      <p>Website www.tinysunnybakes.example</p>
    </div>
  </section>

  <section class="card card--front">
    <svg class="brand-mark" viewBox="0 0 186 156" role="img" aria-label="Bakery logo illustration: a tiered pink cake surrounded by hearts">
      <defs>
        <radialGradient id="markGlow" cx="50%" cy="55%" r="60%">
          <stop offset="0%" stop-color="var(--logo-blush)"/>
          <stop offset="100%" stop-color="var(--logo-pink)" stop-opacity="0.55"/>
        </radialGradient>
      </defs>
      <rect x="0" y="0" width="186" height="156" rx="18" fill="url(#markGlow)"/>
    </svg>
    <p class="brand-name">Tiny Sunny Bakes</p>
  </section>

  <p class="side-label side-label--back">back</p>
  <p class="side-label side-label--front">front</p>
</main>
</body>
</html>
```